Purely Windswept needs an eye catching marketing flyer

Our new Luminous Airflow(r) business needs an eye catching marketing flyer. We think A5 sizing?
website link (where you can understand more about breathwork is www.purelywindswept.co.uk)
Design whatever you would like to design some things that could be of use to mention are below. Will leave it in your capable hands.
Logo files for Purely Windswept attached, use whichever one is best for your design, should be the main logo and colour scheme for the flyer, the second logo is that of Luminous Airflow(r) the breath school who's body of work we will be delivering. This can be anywhere on the flyer
Flyer is needed to get people interested in breathwork, the potential benefits for breathing better
We offer 1:1 sessions, workshops, corporate training
The flyer will have an offer code 'OpenGlow' which will give 15% off the bookers first 1:1 session
Flyer should include the following contact details: Maybe a "find out how breathwork can help you today. . . "
Tessa Orchard (South): 07700 318 527
Lorraine Pitt (Midlands): 07700 452 183
facebook: we.are.purelywindswept
instagram: _purelywindswept_

```html
<!DOCTYPE html>
<html lang="en">
<head>
<meta charset="utf-8">
<title>Purely Windswept – Breathwork Flyer</title>
<link rel="stylesheet" href="https://fonts.googleapis.com/css2?family=Allura&family=Josefin+Sans:wght@400;600;700&display=swap">
<style>
  :root {
    --deep: #051c26;
    --teal: #0f4553;
    --teal-glow: #1b6878;
    --cyan: #4fdcec;
    --blue: #2b63d8;
    --royal: #2a3fae;
    --navy-text: #1b2c4c;
    --ink: #222;
    --white: #ffffff;
    --violet: #6b3fa0;
    --sans: "Josefin Sans", "Century Gothic", sans-serif;
    --script: "Allura", cursive;
  }
  * { margin: 0; padding: 0; box-sizing: border-box; }
  html, body { width: 902px; height: 1200px; overflow: hidden; }
  body { background: var(--deep); font-family: var(--sans); color: var(--white); }

  .flyer { position: relative; width: 902px; height: 1200px; overflow: hidden;
    background: radial-gradient(ellipse 520px 560px at 520px 700px, var(--teal-glow) 0%, var(--teal) 45%, var(--deep) 100%); }

  .backdrop { position: absolute; inset: 0; }

  .brand { position: absolute; left: 517px; top: 86px; width: 244px; height: 244px; border: 2px solid var(--royal);
    border-radius: 50%; display: flex; align-items: center; justify-content: center; text-align: center; }
  .brand-name { font-size: 40px; font-weight: 400; line-height: 1.05; color: var(--white); }

  .why { position: absolute; left: 408px; top: 516px; }
  .why-script { position: absolute; left: 2px; top: -108px; font-family: var(--script); font-size: 112px; line-height: 1; white-space: nowrap; }
  .why-bold { font-size: 46px; font-weight: 700; letter-spacing: 1px; white-space: nowrap; }
  .why-better { position: absolute; left: 244px; top: -20px; font-family: var(--script); font-size: 64px; line-height: 1; white-space: nowrap; }

  .intro { position: absolute; left: 410px; top: 584px; width: 440px; font-size: 18px; line-height: 24px; }

  .benefits { position: absolute; left: 410px; top: 676px; list-style: none; font-size: 16.5px; }
  .benefits li, .offers li { position: relative; padding-left: 26px; }
  .benefits li { height: 31.5px; line-height: 31.5px; }
  .benefits li::before, .offers li::before { content: ""; position: absolute; left: 0; top: 50%; width: 11px; height: 11px;
    margin-top: -7px; border-radius: 50%; background: var(--white); }

  .divider { position: absolute; left: 377px; top: 523px; width: 1.5px; height: 408px; background: rgba(255,255,255,.8); }

  .offers-title { position: absolute; left: 91px; top: 537px; font-size: 29px; font-weight: 400; letter-spacing: 1px; }
  .offers { position: absolute; left: 93px; top: 578px; list-style: none; font-size: 20px; }
  .offers li { height: 32px; line-height: 32px; }

  .offer-ribbon { position: absolute; left: 70px; top: 676px; width: 280px; height: 290px; }
  .offer-text { position: absolute; font-weight: 700; color: var(--white); }
  .offer-label { left: 200px; top: 722px; width: 95px; text-align: right; font-size: 22px; line-height: 24px; }
  .offer-code { left: 97px; top: 787px; font-size: 20px; }
  .offer-detail { left: 97px; top: 816px; font-size: 18px; line-height: 23px; font-weight: 600; }
  .offer-session { left: 97px; top: 864px; font-size: 16px; line-height: 20px; }
  .discount { position: absolute; left: 246px; top: 781px; width: 110px; height: 110px; border-radius: 50%;
    background: var(--white); border: 3px dotted var(--blue); display: flex; align-items: center; justify-content: center;
    color: var(--navy-text); }
  .discount-value { font-size: 40px; font-weight: 700; letter-spacing: -1px; }
  .discount-off { font-size: 15px; font-weight: 700; writing-mode: vertical-rl; margin-left: 2px; }

  .contact { position: absolute; left: 44px; top: 1046px; color: var(--ink); }
  .contact-lead { font-size: 18px; font-weight: 700; line-height: 23px; color: var(--navy-text); margin-bottom: 12px; }
  .contact-line { font-size: 17px; line-height: 21px; }

  .footer-divider { position: absolute; left: 418px; top: 1066px; width: 1.5px; height: 82px; background: var(--ink); }

  .social { position: absolute; left: 439px; top: 1064px; color: var(--ink); }
  .social-title { font-size: 17px; margin-bottom: 10px; }
  .social-line { display: flex; align-items: center; gap: 8px; font-size: 13px; height: 26px; }
  .social-mark { width: 13px; height: 13px; background: var(--ink); border-radius: 2px; }

  .partner { position: absolute; left: 684px; top: 962px; width: 130px; text-align: center; }
  .partner-dot { width: 86px; height: 86px; margin: 0 auto 8px; border-radius: 50%; background: var(--violet); }
  .partner-name { font-size: 12px; color: var(--white); }
</style>
</head>
<body>
<main class="flyer">
  <svg class="backdrop" viewBox="0 0 902 1200" width="902" height="1200" aria-hidden="true">
    <defs>
      <linearGradient id="photoTone" x1="0" y1="0" x2="1" y2="1">
        <stop offset="0" stop-color="#2b2a6e"/>
        <stop offset=".35" stop-color="#8a5a8c"/>
        <stop offset=".6" stop-color="#b57a5a"/>
        <stop offset="1" stop-color="#3a4f9a"/>
      </linearGradient>
      <linearGradient id="photoFade" x1="0" y1="0" x2="1" y2="0">
        <stop offset=".6" stop-color="#fff"/>
        <stop offset="1" stop-color="#000"/>
      </linearGradient>
      <mask id="photoMask"><rect x="0" y="0" width="600" height="560" fill="url(#photoFade)"/></mask>
      <linearGradient id="waveBlue" x1="0" y1="0" x2="1" y2="0">
        <stop offset="0" stop-color="#2b63d8"/>
        <stop offset="1" stop-color="#4fdcec"/>
      </linearGradient>
      <linearGradient id="waveCyan" x1="0" y1="0" x2="1" y2="0">
        <stop offset="0" stop-color="#2b63d8"/>
        <stop offset=".5" stop-color="#4fdcec"/>
        <stop offset="1" stop-color="#6ef0f7"/>
      </linearGradient>
    </defs>

    <g role="img" aria-label="Photograph of a woman with eyes closed breathing in, blended with a starry galaxy">
      <path d="M0,0 H600 V290 C520,310 430,330 395,360 C372,420 330,470 260,492 C170,515 80,500 0,470 Z"
            fill="url(#photoTone)" mask="url(#photoMask)"/>
    </g>

    <path d="M0,430 C120,470 250,480 330,430 C355,414 372,390 385,368 C378,420 350,480 300,505 C220,540 100,520 0,505 Z" fill="url(#waveBlue)"/>
    <path d="M397,402 C520,420 640,340 902,318 V342 C700,352 560,430 397,402 Z" fill="url(#waveCyan)"/>

    <path d="M0,1000 C150,955 390,960 545,968 C600,972 622,995 642,1045 C672,1112 760,1142 902,1152 V1200 H0 Z" fill="#fff"/>
    <path d="M0,998 C150,952 390,956 545,964 C470,958 200,950 0,985 Z" fill="url(#waveBlue)"/>
    <path d="M612,1000 C640,1080 720,1130 902,1138 V1160 C740,1156 650,1120 612,1000 Z" fill="url(#waveCyan)"/>
  </svg>

  <div class="brand"><div class="brand-name">Purely<br>Windswept</div></div>

  <h1 class="why">
    <span class="why-script">Why</span>
    <span class="why-bold">BREATHE</span>
    <span class="why-better">Better</span>
  </h1>

  <p class="intro">You can survive only days without water and only a few weeks without food. Yet without oxygen we can only survive a few minutes.</p>

  <ul class="benefits">
    <li>Our breath removes toxins from our system</li>
    <li>Connected breathing releases muscle tension</li>
    <li>Deep breathing calms the nervous system</li>
    <li>Better breathing improves our mental health</li>
    <li>Breath improves the respiratory system</li>
    <li>Strengthen the lymphatic system</li>
    <li>Breathe for better emotional wellbeing</li>
    <li>Breathing for higher levels of awareness</li>
    <li>Breathe for digestive improvement</li>
  </ul>

  <div class="divider"></div>

  <h2 class="offers-title">WE OFFER</h2>
  <ul class="offers">
    <li>1:1 sessions</li>
    <li>Workshops</li>
    <li>Corporate training</li>
  </ul>

  <svg class="offer-ribbon" viewBox="0 0 280 290" aria-hidden="true">
    <path d="M8,60 L270,12 L270,110 L8,158 Z" fill="#3aaec8"/>
    <path d="M8,60 L230,60 L230,280 L8,280 Z" fill="#2a3fae"/>
    <path d="M20,104 L230,104 L230,138 L20,138 Z" fill="#1c2a78"/>
    <path d="M8,240 C80,250 160,230 270,200 L270,260 L8,286 Z" fill="#3aaec8"/>
    <path d="M8,60 L8,280 L20,286 L20,66 Z" fill="#1c2a78"/>
  </svg>
  <div class="offer-text offer-label">OFFER<br>CODE</div>
  <div class="offer-text offer-code">'OpenGlow'</div>
  <div class="offer-text offer-detail">which will give<br>the bookers</div>
  <div class="offer-text offer-session">FIRST 1:1<br>SESSION</div>
  <div class="discount"><span class="discount-value">15%</span><span class="discount-off">OFF</span></div>

  <div class="contact">
    <p class="contact-lead">Find out how breathwork<br>can help you today. . .</p>
    <p class="contact-line">Tessa Orchard (South): 07700 318 527</p>
    <p class="contact-line">Lorraine Pitt (Midlands): 07700 452 183</p>
  </div>

  <div class="footer-divider"></div>

  <div class="social">
    <p class="social-title">Follow us on</p>
    <p class="social-line"><span class="social-mark"></span>we.are.purelywindswept</p>
    <p class="social-line"><span class="social-mark"></span>_purelywindswept_</p>
  </div>

  <div class="partner">
    <div class="partner-dot"></div>
    <p class="partner-name">Luminous Airflow®</p>
  </div>
</main>
</body>
</html>
```